business card for a massage therapy practice named 'Meadow and Willow Massage Studio'

I really need a trendy, yet easy on the eyes business card to complement my logo. Ideally with some gold or rose gold foil work.

My uploaded file of the logo I have in horizontal but I have a vertical version as well. Another color that is used in the website is a blush pink here and there. I'd like to see some trendy tropical leaves in the design.

```html
<!DOCTYPE html>
<html lang="en">
<head>
<meta charset="utf-8">
<title>Meadow &amp; Willow Massage Studio — Business Card</title>
<link href="https://fonts.googleapis.com/css2?family=Open+Sans:wght@400;600&family=Montserrat:wght@300;400&display=swap" rel="stylesheet">
<style>
  :root {
    --canvas: #e9e6e1;
    --teal-deep: #173538;
    --teal-mid: #2a4e47;
    --leaf-dark: #1f4a3a;
    --leaf-mid: #3f7a55;
    --leaf-light: #6fa86d;
    --bloom: #e0703a;
    --paper: #ecebe7;
    --ink: #2c4a56;
    --rose-gold: #d98a6c;
    --gold: #b8955d;
    --white: #ffffff;
  }
  * { margin: 0; padding: 0; box-sizing: border-box; }
  html, body { width: 1200px; height: 1103px; overflow: hidden; }
  body {
    background: var(--canvas);
    font-family: "Open Sans", Arial, sans-serif;
    position: relative;
  }
  .card {
    position: absolute;
    left: 200px;
    width: 800px;
    height: 457px;
    overflow: hidden;
    box-shadow: 0 6px 22px rgba(0,0,0,0.18);
  }
  .card--front { top: 60px; background: var(--teal-deep); }
  .card--back { top: 586px; }

  /* front */
  .front__photo {
    position: absolute; inset: 0;
    background:
      radial-gradient(ellipse 260px 140px at 18% 30%, rgba(90,120,80,0.55), transparent 70%),
      radial-gradient(ellipse 220px 120px at 82% 62%, rgba(80,110,75,0.5), transparent 70%),
      radial-gradient(ellipse 200px 110px at 60% 20%, rgba(60,95,70,0.45), transparent 70%),
      radial-gradient(ellipse 240px 130px at 30% 85%, rgba(55,90,70,0.45), transparent 70%),
      linear-gradient(160deg, var(--teal-mid), var(--teal-deep) 70%);
  }
  .front__brand {
    position: absolute; left: 0; right: 0; top: 150px;
    text-align: center;
  }
  .front__mark {
    width: 18px; height: 18px; border-radius: 50%;
    background: var(--rose-gold);
    margin: 0 auto 22px;
  }
  .front__name {
    font-family: "Montserrat", Arial, sans-serif;
    font-weight: 400;
    font-size: 46px;
    letter-spacing: 1px;
    color: var(--rose-gold);
  }
  .front__tagline {
    font-family: "Montserrat", Arial, sans-serif;
    font-weight: 300;
    font-size: 17px;
    color: var(--white);
    margin-top: 14px;
  }

  /* back */
  .back__pattern {
    position: absolute; inset: 0;
    background:
      radial-gradient(circle 28px at 4% 45%, var(--bloom), transparent 80%),
      radial-gradient(circle 22px at 97% 14%, var(--bloom), transparent 80%),
      radial-gradient(circle 24px at 33% 96%, var(--bloom), transparent 80%),
      radial-gradient(ellipse 120px 60px at 20% 5%, var(--leaf-light), transparent 75%),
      radial-gradient(ellipse 120px 60px at 75% 97%, var(--leaf-light), transparent 75%),
      radial-gradient(ellipse 80px 140px at 98% 60%, var(--leaf-mid), transparent 75%),
      linear-gradient(135deg, var(--leaf-mid), var(--leaf-dark) 55%, var(--leaf-mid));
  }
  .back__panel {
    position: absolute;
    left: 48px; top: 45px; right: 48px; bottom: 47px;
    background: var(--paper);
  }
  .back__brand {
    position: absolute; left: 0; width: 350px; top: 200px;
    text-align: center;
  }
  .back__mark {
    width: 14px; height: 14px; border-radius: 50%;
    background: var(--gold);
    margin: 0 auto 18px;
  }
  .back__name {
    font-family: "Montserrat", Arial, sans-serif;
    font-weight: 400;
    font-size: 30px;
    color: var(--gold);
  }
  .back__tagline {
    font-family: "Montserrat", Arial, sans-serif;
    font-weight: 300;
    font-size: 14px;
    color: var(--ink);
    margin-top: 10px;
  }
  .back__divider {
    position: absolute; left: 352px; top: 35px; bottom: 40px;
    width: 2px; background: var(--ink);
  }
  .info { position: absolute; left: 366px; top: 36px; right: 10px; color: var(--ink); }
  .info__heading { font-weight: 600; font-size: 14.5px; margin-bottom: 16px; }
  .hours { border-collapse: collapse; font-size: 14px; }
  .hours td { padding: 0; line-height: 19.5px; }
  .hours td:first-child { width: 102px; }
  .info__rule { width: 232px; height: 1px; background: #c9cac6; margin: 12px 0 28px; }
  .contact { border-collapse: collapse; font-size: 13px; }
  .contact th { font-weight: 400; text-align: left; padding: 0 8px 0 0; font-size: 14px; }
  .contact td { padding: 0; line-height: 25px; }
</style>
</head>
<body>

<section class="card card--front" aria-label="Card front">
  <div class="front__photo" role="img" aria-label="Dark moody photograph of tropical leaves with water droplets"></div>
  <div class="front__brand">
    <div class="front__mark"></div>
    <div class="front__name">Meadow &amp; Willow</div>
    <div class="front__tagline">THE MASSAGE STUDIO</div>
  </div>
</section>

<section class="card card--back" aria-label="Card back">
  <div class="back__pattern" role="img" aria-label="Tropical leaves and orange flowers pattern border"></div>
  <div class="back__panel">
    <div class="back__brand">
      <div class="back__mark"></div>
      <div class="back__name">Meadow &amp; Willow</div>
      <div class="back__tagline">THE MASSAGE STUDIO</div>
    </div>
    <div class="back__divider"></div>
    <div class="info">
      <div class="info__heading">Working Hours</div>
      <table class="hours">
        <tr><td>Sunday</td><td>Closed</td></tr>
        <tr><td>Monday</td><td>11:00 AM - 7:00 PM</td></tr>
        <tr><td>Tuesday</td><td>11:00 AM - 7:00 PM</td></tr>
        <tr><td>Wednesday</td><td>11:00 AM - 7:00 PM</td></tr>
        <tr><td>Thursday</td><td>11:00 AM - 7:00 PM</td></tr>
        <tr><td>Friday</td><td>11:00 AM - 7:00 PM</td></tr>
        <tr><td>Saturday</td><td>11:00 AM - 7:00 PM</td></tr>
      </table>
      <div class="info__rule"></div>
      <table class="contact">
        <tr><th>Address:</th><td>418 Linden Avenue, 210, Fairview, CA, 95000</td></tr>
        <tr><th>Phone:</th><td>555-014-2873</td></tr>
        <tr><th>Website:</th><td>www.meadowandwillow.com</td></tr>
      </table>
    </div>
  </div>
</section>

</body>
</html>
```